Brisken. business card

We need a business card design for a new mobile car-wash catered toward urban residents. The use of colour should be black, white and red and should be sleek and minimal. The final design should be modern and enticing to look at. A picture of the logo is attached. The font and design should resemble something similar to the logo.

```html
<!DOCTYPE html>
<html lang="en">
<head>
<meta charset="utf-8">
<title>Brisken. business card</title>
<link rel="stylesheet" href="https://fonts.googleapis.com/css2?family=Open+Sans:wght@400;700&display=swap">
<style>
  :root {
    --backdrop: #3b3b3b;
    --card-black: #0d0d0d;
    --card-glow: #262626;
    --ink-white: #f2f2f2;
    --ink-grey: #bdbdbd;
    --ink-faint: #2e2e2e;
    --accent-red: #d4202b;
  }
  * { box-sizing: border-box; margin: 0; padding: 0; }
  html, body {
    width: 1200px;
    height: 807px;
    overflow: hidden;
  }
  body {
    background: var(--backdrop);
    font-family: "Open Sans", Arial, sans-serif;
    display: flex;
    align-items: center;
    justify-content: center;
    gap: 60px;
  }
  .card {
    position: relative;
    width: 510px;
    height: 300px;
    border-radius: 4px;
    background: radial-gradient(ellipse at 45% 45%, var(--card-glow) 0%, var(--card-black) 70%);
    box-shadow: 0 10px 30px rgba(0, 0, 0, 0.45);
    overflow: hidden;
  }

  /* Front: tone-on-tone brand name */
  .card--front .brand-emboss {
    position: absolute;
    right: 70px;
    top: 120px;
    display: flex;
    align-items: center;
    gap: 10px;
    font-size: 40px;
    font-weight: 700;
    letter-spacing: 4px;
    color: var(--ink-faint);
  }
  .brand-emboss .brand-dot {
    width: 12px;
    height: 12px;
    background: var(--ink-faint);
  }

  /* Back: brand block and contact details */
  .card--back .brand-block {
    position: absolute;
    left: 48px;
    top: 110px;
  }
  .brand-name {
    display: flex;
    align-items: center;
    gap: 10px;
    font-size: 40px;
    font-weight: 700;
    letter-spacing: 4px;
    color: var(--ink-white);
  }
  .brand-name .brand-dot {
    width: 12px;
    height: 12px;
    background: var(--accent-red);
  }
  .brand-tagline {
    margin-top: 6px;
    font-size: 14px;
    font-weight: 700;
    letter-spacing: 2px;
    text-transform: uppercase;
    color: var(--ink-white);
  }
  .contact {
    position: absolute;
    right: 34px;
    top: 92px;
    width: 160px;
    color: var(--ink-grey);
    font-size: 11px;
    line-height: 1.5;
  }
  .contact .person-name {
    font-size: 14px;
    color: var(--ink-white);
    line-height: 1.2;
  }
  .contact .person-title {
    color: var(--accent-red);
    font-size: 11px;
    margin-bottom: 18px;
  }
  .contact .label {
    color: var(--accent-red);
    font-weight: 700;
  }
  .contact .address {
    margin-top: 16px;
  }
</style>
</head>
<body>
  <div class="card card--front">
    <div class="brand-emboss">Brisken.<span class="brand-dot"></span></div>
  </div>

  <div class="card card--back">
    <div class="brand-block">
      <div class="brand-name">Brisken.<span class="brand-dot"></span></div>
      <div class="brand-tagline">Mobile Car Finishing</div>
    </div>
    <div class="contact">
      <p class="person-name">Your Name</p>
      <p class="person-title">Title</p>
      <p><span class="label">P:</span> +1 12345-67890</p>
      <p><span class="label">E:</span> info@brisken-mobile.com</p>
      <p><span class="label">W:</span> www.brisken-mobile.com</p>
      <p class="address">321 Main Avenue,<br>NY 100 P.O.Box: 12345</p>
    </div>
  </div>
</body>
</html>
```